1923 Basins & Spouts Business Card

I'm wanting to get a business card designed. Our business is 1923 Basins & Spouts
Details for the card:

1923 Basins & Spouts
Name: Gareth Vostle
Email: gareth@1923basinsandspouts.com.au
Website: www.1923basinsandspouts.com.au
Mobile: 0439 602 158
Phone: 02 5550 1843

Font of Basins & Spouts is called Snell Roundhand. Not sue what font logo text is.

I'm thinking two sided but it doesn't have to be.

```html
<!DOCTYPE html>
<html lang="en">
<head>
<meta charset="utf-8">
<title>1923 Basins &amp; Spouts – Business Card</title>
<link rel="stylesheet" href="https://fonts.googleapis.com/css2?family=Great+Vibes&family=Kaushan+Script&family=Open+Sans:wght@400;700&display=swap">
<style>
  :root {
    --backdrop: #e4e4e2;
    --card: #ffffff;
    --ink: #111111;
    --ink-soft: #444444;
    --ornament-grey: #cdcdcd;
    --ornament-grey-light: #ececec;
    --ornament-dark: #1e1e1e;
    --shadow: rgba(0, 0, 0, 0.18);
  }
  * { box-sizing: border-box; margin: 0; padding: 0; }
  html, body {
    width: 1200px;
    height: 800px;
    overflow: hidden;
    background: var(--backdrop);
  }
  .sheet {
    position: relative;
    width: 1200px;
    height: 800px;
    display: flex;
    align-items: center;
    justify-content: center;
    gap: 40px;
  }
  .card {
    position: relative;
    width: 540px;
    height: 309px;
    background: var(--card);
    box-shadow: 0 6px 18px var(--shadow);
    overflow: hidden;
  }

  /* Brand mark placeholder: plain circle + company name */
  .brand-mark {
    position: absolute;
    display: flex;
    align-items: center;
    gap: 10px;
    width: 150px;
  }
  .brand-mark__circle {
    flex: none;
    width: 42px;
    height: 42px;
    border: 2px solid var(--ink);
    border-radius: 50%;
  }
  .brand-mark__name {
    font-family: "Open Sans", sans-serif;
    font-weight: 400;
    font-size: 13px;
    line-height: 1.3;
    color: var(--ink);
  }

  /* Front */
  .front .brand-mark { left: 28px; top: 132px; }
  .front__text {
    position: absolute;
    left: 178px;
    top: 118px;
  }
  .front__title {
    font-family: "Great Vibes", cursive;
    font-weight: 400;
    font-size: 38px;
    line-height: 1;
    color: var(--ink);
  }
  .front__tagline {
    margin-top: 8px;
    font-family: "Open Sans", sans-serif;
    font-size: 8.5px;
    color: var(--ink-soft);
  }
  .front__flourish {
    position: absolute;
    left: 370px;
    top: 0;
    width: 170px;
    height: 100%;
    background: linear-gradient(to right, rgba(255,255,255,0), var(--ornament-grey-light) 30%, var(--ornament-grey) 65%, var(--ornament-grey-light));
  }

  /* Back */
  .back .brand-mark { left: 36px; top: 100px; }
  .back__name {
    position: absolute;
    left: 236px;
    top: 74px;
    font-family: "Kaushan Script", cursive;
    font-weight: 400;
    font-size: 24px;
    color: var(--ink);
  }
  .back__rule {
    position: absolute;
    left: 190px;
    top: 116px;
    width: 150px;
    height: 2px;
    background: linear-gradient(to right, rgba(17,17,17,0), var(--ink) 60%, rgba(17,17,17,0));
  }
  .contact-list {
    position: absolute;
    left: 236px;
    top: 128px;
    list-style: none;
    font-family: "Open Sans", sans-serif;
    font-size: 11px;
    color: var(--ink);
  }
  .contact-list li {
    display: flex;
    align-items: center;
    gap: 8px;
    height: 20px;
  }
  .contact-list .icon {
    width: 14px;
    height: 14px;
    flex: none;
  }
  .contact-list .website {
    font-weight: 700;
    font-size: 11.5px;
    padding-left: 22px;
  }
  .back__border {
    position: absolute;
    left: 0;
    bottom: 0;
    width: 100%;
    height: 46px;
    background: linear-gradient(to bottom, rgba(30,30,30,0.25), var(--ornament-dark) 55%);
  }
</style>
</head>
<body>
<main class="sheet">

  <section class="card front" aria-label="Card front">
    <div class="brand-mark">
      <span class="brand-mark__circle"></span>
      <span class="brand-mark__name">1923 Basins<br>&amp; Spouts</span>
    </div>
    <div class="front__text">
      <h1 class="front__title">Basins &amp; Spouts</h1>
      <p class="front__tagline">Combining timeless beauty with perfect practicality</p>
    </div>
    <div class="front__flourish" role="img" aria-label="Soft grey leafy swirl ornament"></div>
  </section>

  <section class="card back" aria-label="Card back">
    <div class="brand-mark">
      <span class="brand-mark__circle"></span>
      <span class="brand-mark__name">1923 Basins<br>&amp; Spouts</span>
    </div>
    <h2 class="back__name">Gareth Vostle</h2>
    <div class="back__rule"></div>
    <ul class="contact-list">
      <li>
        <svg class="icon" viewBox="0 0 14 14" aria-hidden="true">
          <rect width="14" height="14" rx="3" fill="#111"/>
          <rect x="4.5" y="2.5" width="5" height="9" rx="1" fill="none" stroke="#fff" stroke-width="1.2"/>
        </svg>
        <span>0439 602 158</span>
      </li>
      <li>
        <svg class="icon" viewBox="0 0 14 14" aria-hidden="true">
          <circle cx="7" cy="7" r="7" fill="#111"/>
          <path d="M4 9.5h6v-2.5l-1.5-2h-3l-1.5 2z" fill="#fff"/>
          <rect x="4" y="4" width="6" height="1.2" fill="#fff"/>
        </svg>
        <span>02 5550 1843</span>
      </li>
      <li>
        <svg class="icon" viewBox="0 0 14 14" aria-hidden="true">
          <rect width="14" height="14" rx="3" fill="#111"/>
          <rect x="3" y="4.5" width="8" height="5.5" fill="none" stroke="#fff" stroke-width="1"/>
          <path d="M3 4.5l4 3 4-3" fill="none" stroke="#fff" stroke-width="1"/>
        </svg>
        <span>gareth@1923basinsandspouts.com.au</span>
      </li>
      <li><span class="website">www.1923basinsandspouts.com.au</span></li>
    </ul>
    <div class="back__border" role="img" aria-label="Black climbing vine ornament border"></div>
  </section>

</main>
</body>
</html>
```